upolstery Business Card Design

Antique furniture restoration, motor and marine trimming, canvas work ,cafe blinds,

Industry/Entity Type

Business

Contact Information for Business Card

KR UPOLSTERY & CANVAS
42 LOBB ST DENHAM
Colin Ashgrove PH:0491355206
ashg81@larkmail.com

```html
<!DOCTYPE html>
<html lang="en">
<head>
<meta charset="utf-8">
<title>KR Upolstery &amp; Canvas — Business Card</title>
<link href="https://fonts.googleapis.com/css2?family=Cinzel:wght@400;500&family=Open+Sans:wght@400;700&display=swap" rel="stylesheet">
<style>
  :root {
    --page: #ffffff;
    --wood-dark: #2a130c;
    --wood-mid: #4a2416;
    --wood-warm: #5c2d1b;
    --ivory: #f4f1ec;
    --ink-light: #ffffff;
    --rule: rgba(255,255,255,0.55);
  }
  html, body {
    margin: 0;
    width: 1200px;
    height: 1200px;
    overflow: hidden;
    background: var(--page);
  }
  .canvas {
    position: relative;
    width: 1200px;
    height: 1200px;
    display: flex;
    align-items: center;
    justify-content: center;
  }
  .card {
    position: relative;
    width: 1000px;
    height: 572px;
    overflow: hidden;
    background:
      linear-gradient(90deg, rgba(0,0,0,0.18) 0%, rgba(0,0,0,0) 30%, rgba(90,40,20,0.25) 55%, rgba(0,0,0,0.15) 100%),
      linear-gradient(180deg, var(--wood-mid) 0%, var(--wood-warm) 45%, var(--wood-dark) 100%);
    box-shadow: 0 4px 18px rgba(0,0,0,0.18);
  }
  .chair {
    position: absolute;
    background: var(--ivory);
  }
  .chair--left {
    left: 0;
    top: 0;
    width: 235px;
    height: 450px;
    border-radius: 0 90px 60px 0;
  }
  .chair--right {
    right: 0;
    bottom: 0;
    width: 230px;
    height: 460px;
    border-radius: 90px 0 0 60px;
  }
  .brand {
    position: absolute;
    left: 250px;
    width: 500px;
    top: 40px;
    text-align: center;
    color: var(--ink-light);
  }
  .brand__name {
    font-family: "Cinzel", serif;
    font-weight: 400;
    font-size: 140px;
    line-height: 1;
    letter-spacing: 2px;
    margin: 0;
  }
  .brand__rule {
    width: 360px;
    height: 1px;
    background: var(--rule);
    margin: 8px auto 10px;
  }
  .brand__trade {
    font-family: "Cinzel", serif;
    font-size: 34px;
    letter-spacing: 1px;
    margin: 0;
  }
  .contact {
    position: absolute;
    left: 270px;
    top: 345px;
    color: var(--ink-light);
    font-family: "Open Sans", sans-serif;
  }
  .contact__address {
    font-family: "Cinzel", serif;
    font-weight: 500;
    font-size: 38px;
    margin: 0 0 4px;
    letter-spacing: 1px;
  }
  .contact__line {
    display: flex;
    align-items: center;
    gap: 12px;
    margin: 2px 0;
  }
  .contact__line svg { width: 22px; height: 22px; flex: none; }
  .contact__email { font-size: 22px; font-weight: 400; }
  .contact__phone { font-size: 28px; font-weight: 700; letter-spacing: 1px; }
</style>
</head>
<body>
<div class="canvas">
  <section class="card">
    <div class="chair chair--left" role="img" aria-label="Ornate antique armchair illustration in white line art"></div>
    <div class="chair chair--right" role="img" aria-label="Ornate antique armchair illustration in white line art"></div>

    <header class="brand">
      <h1 class="brand__name">KR</h1>
      <div class="brand__rule"></div>
      <p class="brand__trade">Upolstery &amp; Canvas</p>
    </header>

    <address class="contact" style="font-style:normal">
      <p class="contact__address">42 LOBB ST DENHAM</p>
      <div class="contact__line">
        <svg viewBox="0 0 24 24" aria-hidden="true"><rect x="2" y="5" width="20" height="14" rx="1.5" fill="#fff"/><path d="M2.5 5.5 12 13l9.5-7.5" fill="none" stroke="#3a1a10" stroke-width="1.6"/></svg>
        <span class="contact__email">ashg81@larkmail.com</span>
      </div>
      <div class="contact__line">
        <svg viewBox="0 0 24 24" aria-hidden="true"><circle cx="12" cy="12" r="10" fill="none" stroke="#fff" stroke-width="2"/><path d="M9 7c-1 1-1.2 2.5 0 4.8 1.2 2.4 2.8 4 5 5 1.2.5 2-.1 2.6-.9l-1.8-1.6-1.3.7c-1-.6-2.1-1.8-2.6-2.9l.8-1.2L10.4 7z" fill="#fff"/></svg>
        <span class="contact__phone">0491 355 206</span>
      </div>
    </address>
  </section>
</div>
</body>
</html>
```